Velmora Design

Looking for Velmora banner and square design:
Velmora Banner
W:1600 px H:400 px
Square
120x120

Logo attached.

Description: Data-Driven stock market portfolio management using quantitative analysis.

```html
<!DOCTYPE html>
<html lang="en">
<head>
<meta charset="utf-8">
<title>Velmora – Square and Banner</title>
<link href="https://fonts.googleapis.com/css2?family=Poppins:wght@400;500;600&display=swap" rel="stylesheet">
<style>
  :root {
    --canvas: #e4e4e4;
    --brand-blue: #0b77b9;
    --brand-blue-deep: #0a65a3;
    --ink-navy: #1b3f6b;
    --white: #ffffff;
    --halo: #dcecfa;
    --halo-edge: #bcdaf3;
  }
  * { margin: 0; padding: 0; box-sizing: border-box; }
  html, body { width: 1200px; height: 1200px; overflow: hidden; }
  body {
    background: var(--canvas);
    font-family: "Poppins", sans-serif;
    position: relative;
  }
  .piece { position: absolute; overflow: hidden; background: var(--brand-blue); }
  .piece-square { left: 374px; top: 204px; width: 453px; height: 453px; }
  .piece-banner { left: 28px; top: 684px; width: 1146px; height: 286px; }
  .piece svg.backdrop { position: absolute; inset: 0; }

  .brand {
    position: absolute;
    display: flex;
    align-items: center;
    gap: 10px;
    color: var(--ink-navy);
    font-weight: 500;
    letter-spacing: 0.5px;
    line-height: 1;
  }
  .brand-dot { background: var(--brand-blue); border-radius: 50%; flex: none; }
  .piece-square .brand { left: 92px; top: 24px; font-size: 20px; }
  .piece-square .brand-dot { width: 26px; height: 26px; }
  .piece-banner .brand { left: 124px; top: 30px; font-size: 26px; }
  .piece-banner .brand-dot { width: 34px; height: 34px; }

  .artwork {
    position: absolute;
    border-radius: 50%;
    background: radial-gradient(circle at 50% 50%, #f3f9ff 0%, var(--halo) 65%, var(--halo-edge) 100%);
  }
  .piece-square .artwork { left: 130px; top: 58px; width: 310px; height: 240px; }
  .piece-banner .artwork { left: 700px; top: 6px; width: 360px; height: 272px; }

  .headline { position: absolute; color: var(--brand-blue-deep); line-height: 1.15; }
  .headline h1 { font-weight: 600; }
  .headline p { font-weight: 400; }
  .piece-square .headline { left: 76px; top: 300px; }
  .piece-square .headline h1 { font-size: 28px; }
  .piece-square .headline p { font-size: 16.5px; letter-spacing: 0.3px; line-height: 1.15; }
  .piece-banner .headline { left: 122px; top: 86px; }
  .piece-banner .headline h1 { font-size: 49px; line-height: 1.05; }
  .piece-banner .headline p { font-size: 29px; letter-spacing: 0.4px; line-height: 1.1; }
</style>
</head>
<body>

<section class="piece piece-square">
  <svg class="backdrop" width="453" height="453" viewBox="0 0 453 453">
    <path d="M82,0 L453,0 L453,362 Q250,392 86,453 Q-20,230 82,0 Z" fill="var(--white)"/>
  </svg>
  <div class="brand"><span class="brand-dot"></span>VELMORA</div>
  <div class="artwork" role="img" aria-label="Isometric illustration of two analysts working with a dashboard screen, servers and data devices"></div>
  <div class="headline">
    <h1>Data-Driven</h1>
    <p>stock market portfolio management<br>using quantitative analysis.</p>
  </div>
</section>

<section class="piece piece-banner">
  <svg class="backdrop" width="1146" height="286" viewBox="0 0 1146 286">
    <path d="M62,0 L1056,0 Q1118,143 1062,286 L720,286 Q400,170 88,286 Q22,143 62,0 Z" fill="var(--halo-edge)"/>
    <path d="M69,0 L1050,0 Q1108,143 1055,286 L712,286 Q400,172 94,286 Q32,143 69,0 Z" fill="var(--white)"/>
  </svg>
  <div class="brand"><span class="brand-dot"></span>VELMORA</div>
  <div class="headline">
    <h1>Data-Driven</h1>
    <p>stock market portfolio management<br>using quantitative analysis.</p>
  </div>
  <div class="artwork" role="img" aria-label="Isometric illustration of two analysts working with a dashboard screen, servers and data devices"></div>
</section>

</body>
</html>
```